Fun and Flirty Urban Fiction Book Needs a Book Cover Design

We need an e-book cover designed for a title called Dazzle Dazzle SEQUIN STORM.

We require:

1. 3 sexy and provocative African-American female models who look similar to the girl in the green shorts on the cover provided entitled Cool Cat Charmer.

2. A set of beautiful and shapely twins (they are the Dazzle Dazzle in the title) and then an equally shapely and beautiful model in scanty attire (she is the SEQUIN STORM) in the title.

3. We need vibrant and sexy colors and dynamic fonts, whose FONT examples are provided in the upload.

Very Important!

1. The fonts for the words Dazzle Dazzle should match the font for the word Liar on the green cover attached. (Cool Cat Charmer).

2. The fonts for the words Sequin Storm must match the fonts for the words Sequin Storm on the orange cover attached. (Sequin Storm).

3. The cover colors must be vibrant and upbeat. This is a FUN and "flirty" novel.

4. The author's names should appear as by Velour and Tasha Bay.

Please look at the series of bookcovers that are attached!!!

5. The cover must fit in with the theme of the book covers provided. That means, there must be some white on the cover, on the right hand side, and then faded into the rest of the background.

6. The title should take up a large portion of the cover, as it does in the covers provided.

7. The sub-title should say: The Escapades of Coco Delane featuring Peachee Kane. See fonts on the covers provided.

8. The author name VELOUR must be in the same font as on the covers provided, preferably in 3D with the words Vantage Bestselling Author above it.

9. The author name Tasha Bay can be in a different font.

DESIGNERS SHOULD LOOK AT EXAMPLE COVERS AND FONTS PROVIDED AND MAKE THIS COVER FIT INTO THE THEME OF THE PREVIOUS BOOKS.

Target Market(s)

Fiction readers ages 18-50.

Font styles to use
Script
Other font styles liked:
• Fonts similar to those provided in the upload

Requirements
Must have
• Please look at the series of bookcovers that are attached!!!
• 1. The cover must fit in with the theme of the book covers provided. That means, there must be some white on the cover, on the right hand side, and then faded into the rest of the background.
• 2. The title should take up a large portion of the cover, as it does in the covers provided.
• 3. The sub-title should say: The Escapades of Coco Delane featuring Peachee Kane
• 4. The author name VELOUR must be in the same font as on the covers provided, preferably in 3D.
• 5. The author name Tasha Bay can be in a different font.
• Three beautiful biracial or African American female models who look similar to the girl described on the green book titled COOL CAT CHARMER. Fonts similar to those provided in the project description. A fun, sexy, urban flair.
Nice to have
• Shapely, devious and beautiful models
Should not have
• Thin models who are not either bi-racial or African American.

```html
<!DOCTYPE html>
<html lang="en">
<head>
<meta charset="utf-8">
<title>Dazzle Dazzle SEQUIN STORM — Cover</title>
<link rel="stylesheet" href="https://fonts.googleapis.com/css2?family=Pinyon+Script&family=Cinzel:wght@500;600&family=Tinos&display=swap">
<style>
  :root {
    --page-bg: #e3e5e8;
    --cover-bg: #b9a89f;
    --figure-dark: #1d1a2a;
    --figure-mid: #3b2a4e;
    --splash-magenta: #b0307e;
    --splash-blue: #2f6f9a;
    --splash-lime: #c9c26a;
    --gold-light: #fff6d8;
    --gold-mid: #e3c886;
    --gold-deep: #a9874a;
    --text-white: #ffffff;
  }
  * { margin: 0; padding: 0; box-sizing: border-box; }
  html, body {
    width: 1200px;
    height: 1200px;
    overflow: hidden;
    background: var(--page-bg);
  }
  .cover {
    position: absolute;
    left: 176px;
    top: 44px;
    width: 848px;
    height: 1112px;
    background: var(--cover-bg);
    overflow: hidden;
  }
  .cover-art {
    position: absolute;
    inset: 0;
    width: 100%;
    height: 100%;
  }
  .title-block {
    position: absolute;
    left: 0;
    top: 0;
    width: 100%;
    height: 100%;
  }
  .gold {
    background: linear-gradient(180deg, var(--gold-light) 0%, var(--gold-mid) 45%, var(--gold-deep) 70%, var(--gold-light) 100%);
    -webkit-background-clip: text;
    background-clip: text;
    color: transparent;
    filter: drop-shadow(2px 3px 2px rgba(20, 10, 20, 0.55));
  }
  .title-script {
    position: absolute;
    font-family: "Pinyon Script", cursive;
    font-size: 150px;
    line-height: 1;
    white-space: nowrap;
  }
  .title-script--first { left: 170px; top: 262px; }
  .title-script--second { left: 270px; top: 410px; }
  .title-caps {
    position: absolute;
    left: 180px;
    width: 480px;
    text-align: center;
    font-family: "Cinzel", serif;
    font-weight: 600;
    line-height: 1;
    white-space: nowrap;
  }
  .title-caps--top { top: 600px; font-size: 104px; }
  .title-caps--bottom { top: 706px; font-size: 108px; }
  .authors {
    position: absolute;
    left: 180px;
    width: 480px;
    top: 822px;
    text-align: center;
    font-family: "Tinos", serif;
    font-size: 32px;
    color: var(--text-white);
    text-shadow: 1px 1px 2px rgba(0, 0, 0, 0.4);
  }
</style>
</head>
<body>
  <main class="cover">
    <svg class="cover-art" viewBox="0 0 848 1112" role="img" aria-label="Photo of a posing woman in low-rise briefs, inverted tones, with magenta, blue and lime paint splashes behind her">
      <defs>
        <radialGradient id="figureTone" cx="0.5" cy="0.55" r="0.55">
          <stop offset="0" stop-color="var(--figure-dark)"/>
          <stop offset="0.35" stop-color="var(--figure-mid)"/>
          <stop offset="0.6" stop-color="var(--splash-magenta)" stop-opacity="0.55"/>
          <stop offset="0.8" stop-color="var(--splash-blue)" stop-opacity="0.2"/>
          <stop offset="1" stop-color="var(--cover-bg)" stop-opacity="0"/>
        </radialGradient>
      </defs>
      <rect x="0" y="40" width="848" height="1072" fill="url(#figureTone)"/>
    </svg>

    <div class="title-block">
      <h1>
        <span class="title-script title-script--first gold">Dazzle</span>
        <span class="title-script title-script--second gold">Dazzle</span>
        <span class="title-caps title-caps--top gold">SEQUIN</span>
        <span class="title-caps title-caps--bottom gold">STORM</span>
      </h1>
      <p class="authors">Velour and Tasha Bay</p>
    </div>
  </main>
</body>
</html>
```